New Wordpress Website

We need a new wordpress website for our IT Association. Our main corporate colour is orange. Style Guideline attached.
The association is an NFP for IT Professionals. An opportunity for our members to collaborate and grow as a community.

Current website can be found at: www.crestlanetechguild.org

Target Market(s)

IT Professionals and Small Business Owners who need IT Information

Industry/Entity Type

Information Technology

Coding

Coded - Design and coding required

Colors
f37122

```html
<!DOCTYPE html>
<html lang="en">
<head>
<meta charset="utf-8">
<title>Crestlane Tech Guild</title>
<link href="https://fonts.googleapis.com/css2?family=Open+Sans:wght@300;400;600&display=swap" rel="stylesheet">
<style>
:root{
  --orange:#f37122;
  --ink:#3a3a3a;
  --muted:#8a8a8a;
  --line:#e4e4e4;
  --paper:#ffffff;
  --mist:#f6f6f6;
  --night:#2b2b2b;
}
*{box-sizing:border-box;margin:0;padding:0}
html,body{width:1200px;height:4768px;overflow:hidden}
body{position:relative;background:var(--paper);font-family:"Open Sans",Arial,sans-serif;color:var(--ink)}
.abs{position:absolute}
.btn{display:inline-block;border:2px solid var(--orange);border-radius:30px;font-size:15px;padding:8px 24px;color:var(--ink);background:#fff;white-space:nowrap}
.btn.solid{background:var(--orange);color:#fff}
.eyebrow{color:var(--orange);font-size:16px}
.light-h{font-weight:300;color:var(--ink)}
.small{font-size:14px;line-height:1.7;color:var(--muted)}

/* header */
.site-header{left:0;top:0;width:1200px;height:76px;background:#fff;z-index:3}
.brand{left:160px;top:18px;display:flex;align-items:center;gap:10px;font-weight:600;font-size:22px;color:var(--ink)}
.brand-dot{width:34px;height:34px;border-radius:50%;background:var(--orange)}
.nav{left:384px;top:28px;display:flex;gap:22px;font-size:13px;color:var(--ink);white-space:nowrap}
.nav-join{left:950px;top:20px;padding:6px 18px;font-size:13px}

/* hero */
.hero{left:0;top:76px;width:1200px;height:684px;border-bottom-left-radius:140px;overflow:hidden;
  background:linear-gradient(120deg,#6b6560 0%,#b7aea4 35%,#d9d3cc 55%,#5c5550 85%,#3c3835 100%)}
.hero h1{left:264px;top:250px;font-weight:300;font-size:60px;line-height:1.05;color:#fff}
.hero .btn{left:264px;top:396px;border-color:var(--orange)}
.hero .brochure{left:264px;top:490px;display:flex;align-items:center;gap:24px;color:#fff;font-size:16px}
.hero .brochure span.ico{width:40px;height:40px;border:2px solid #fff;border-radius:50%;display:flex;align-items:center;justify-content:center}

/* partners */
.partners-label{left:0;width:1200px;top:830px;text-align:center}
.partner-row{left:180px;width:840px;display:flex;justify-content:space-around;align-items:center;font-weight:600;font-size:22px;color:#9a9a9a}
.partner-badge{width:58px;height:58px;border-radius:50%;background:#d8d8d8}

/* lower background */
.mist{left:0;top:1080px;width:1200px;height:3220px;background:var(--mist)}
.sweep{left:0;top:1080px}

/* about */
.grow{left:256px;top:1180px;font-size:50px;line-height:1.15}
.video-back{left:152px;top:1680px;width:240px;height:176px;background:var(--orange)}
.video{left:176px;top:1336px;width:424px;height:424px;border-radius:0 0 80px 0;
  background:linear-gradient(135deg,#c7cdd3,#8f9aa4 50%,#e7dfd6)}
.play{left:356px;top:1516px}
.about{left:700px;top:1372px;width:340px}
.about .lead{font-size:17px;line-height:1.55;color:var(--ink);margin:26px 0 20px}
.about .btn{margin-top:28px;font-size:14px;padding:6px 18px}

/* pillars */
.pillars{left:256px;top:1950px;width:664px}
.pillar{display:flex;gap:30px;padding:22px 0;border-bottom:1px solid var(--line)}
.pillar:last-child{border-bottom:none}
.pillar h3{font-size:20px;font-weight:400;margin-bottom:6px}
.pillar p{font-size:13px;line-height:1.6;color:var(--muted)}
.pillars-cta{left:510px;top:2372px;font-size:14px;padding:6px 20px}

/* chapters */
.chapters{left:256px;top:2596px;width:300px}
.chapters h2{font-size:22px;line-height:1.4;margin:26px 0 20px}
.chapters .btn{margin-top:22px;font-size:14px;padding:6px 16px}
.city{left:608px;top:2504px;width:440px;height:496px;border-radius:0 0 80px 0;
  background:linear-gradient(180deg,#9fb8d2 0%,#c9d4df 40%,#7a8a7c 70%,#4f5f53 100%)}
.city-strip{left:1048px;top:2660px;width:26px;height:260px;background:var(--orange)}

/* testimonial */
.section-h{left:0;width:1200px;text-align:center;font-size:46px;font-weight:300}
.portrait-ring{left:252px;top:3204px}
.portrait{left:272px;top:3224px;width:208px;height:208px;border-radius:50%;background:linear-gradient(160deg,#e8e8e8,#9aa3ab)}
.quote-mark{left:524px;top:3196px;font-size:54px;color:var(--orange);font-weight:600}
.quote{left:580px;top:3212px;width:460px;font-size:17px;line-height:1.7;color:var(--muted)}
.quote cite{display:block;font-style:normal;font-size:13px;color:var(--ink);margin-top:22px;line-height:1.6}
.dots{left:560px;top:3500px;display:flex;gap:12px}
.dots i{width:11px;height:11px;border-radius:50%;background:#bdbdbd;display:block}
.dots i.on{background:var(--orange)}

/* news */
.news-h{left:256px;top:3640px;font-size:46px;font-weight:300}
.news-card{top:3760px;width:276px;height:400px;background:#fff;border-radius:0 0 48px 0;overflow:hidden}
.news-card .pic{height:290px}
.news-card .body{padding:16px 20px}
.news-card .date{font-size:12px;color:var(--orange)}
.news-card h4{font-size:15px;font-weight:400;line-height:1.4;margin-top:6px}

/* footer */
.footer{left:0;top:4300px;width:1200px;height:468px;background:var(--night);border-top-left-radius:140px;color:#fff}
.footer .pitch{left:256px;top:72px;width:420px}
.footer .pitch strong{display:block;font-size:20px;font-weight:400;margin-bottom:6px}
.footer .pitch p{font-size:14px;line-height:1.6;color:#cfcfcf}
.footer .btn{top:84px;font-size:14px;padding:7px 20px;color:#fff;background:transparent}
.footer .btn.solid{background:var(--orange)}
.footer .rule{left:176px;top:212px;width:856px;height:1px;background:#555}
.footer .col{top:250px;font-size:14px;color:#cfcfcf;line-height:1.7}
.footer .col h5{color:var(--orange);font-size:15px;font-weight:400;margin-bottom:14px}
.footer .phone{font-size:24px;color:#fff}
.socials{display:flex;gap:14px}
.socials i{width:32px;height:32px;border-radius:50%;border:1px solid #999;display:block}
</style>
</head>
<body>

<header class="site-header abs">
  <div class="brand abs"><span class="brand-dot"></span>Crestlane</div>
  <nav class="nav abs"><span>How It Works</span><span>Chapters</span><span>Members</span><span>Partners</span><span>Media</span><span>Events</span><span>About</span></nav>
  <span class="btn nav-join abs">Join Us</span>
</header>

<section class="hero abs" role="img" aria-label="Photo of business professionals gathered around a meeting table">
  <h1 class="abs">Strength<br>in numbers.</h1>
  <span class="btn solid abs">Join Us Today</span>
  <div class="brochure abs"><span class="ico"><svg width="16" height="16" viewBox="0 0 16 16"><path d="M8 2v9M4 7l4 4 4-4M3 14h10" stroke="#fff" stroke-width="1.6" fill="none"/></svg></span>Download Brochure</div>
</section>

<div class="eyebrow partners-label abs">Key Partners</div>
<div class="partner-row abs" style="top:890px"><span>Norbridge</span><span>Kelvo</span><span>Swiftmark</span><span>Rootline</span></div>
<div class="partner-row abs" style="top:968px;left:300px;width:600px"><span class="partner-badge"></span><span class="partner-badge"></span><span class="partner-badge"></span><span class="partner-badge"></span></div>

<div class="mist abs"></div>
<svg class="sweep abs" width="1200" height="170" viewBox="0 0 1200 170"><path d="M0 0 L1200 0 L1200 160 C 900 60 300 80 0 0 Z" fill="#ffffff" opacity="0.7"/></svg>

<h2 class="grow light-h abs">Grow your business, Grow<br>your reputation.</h2>
<div class="video-back abs"></div>
<div class="video abs" role="img" aria-label="Video still of colleagues collaborating at a desk"></div>
<svg class="play abs" width="64" height="64" viewBox="0 0 64 64"><path d="M18 8 L54 32 L18 56 Z" fill="none" stroke="#fff" stroke-width="3"/></svg>
<div class="about abs">
  <div class="eyebrow">About Company</div>
  <p class="lead">Crestlane Tech Guild is Australia's leading industry association for IT business owners and professionals specialising in IT solutions for small and medium business.</p>
  <p class="small">As a member you can draw upon, and add to, the collective knowledge base of best-practice solutions and expert opinions gathered from a national network of IT business owners and professionals.</p>
  <span class="btn">About Us</span>
</div>

<div class="pillars abs">
  <div class="pillar">
    <svg width="40" height="40" viewBox="0 0 40 40"><circle cx="17" cy="17" r="11" fill="none" stroke="#f37122" stroke-width="2.5"/><path d="M25 25l10 10" stroke="#f37122" stroke-width="2.5"/></svg>
    <div><h3>Seek.</h3><p>Connect over time and find proven IT solutions tried and tested by members. Earn peer advice to build practical IT solutions specifically...</p></div>
  </div>
  <div class="pillar">
    <svg width="40" height="40" viewBox="0 0 40 40"><circle cx="20" cy="20" r="8" fill="none" stroke="#f37122" stroke-width="2.5"/><circle cx="20" cy="20" r="15" fill="none" stroke="#f37122" stroke-width="2.5" stroke-dasharray="6 4"/></svg>
    <div><h3>Solve.</h3><p>Create a more efficient and effective business, and deliver greater value to your customers via best-practice problem solving...</p></div>
  </div>
  <div class="pillar">
    <svg width="40" height="40" viewBox="0 0 40 40"><path d="M20 5 L35 32 L5 32 Z" fill="none" stroke="#f37122" stroke-width="2.5"/><path d="M14 22l6-6 6 6" fill="none" stroke="#f37122" stroke-width="2.5"/></svg>
    <div><h3>Share.</h3><p>Join the collective buying power and influence of Australia's largest industry association for small and medium business IT...</p></div>
  </div>
</div>
<span class="btn pillars-cta abs">Contact Us Today</span>

<div class="chapters abs">
  <div class="eyebrow">Chapters</div>
  <h2 class="light-h">Find your local Crestlane Tech Guild Chapter.</h2>
  <p class="small">Grow your professional network and knowledge at our Chapter meetings. Featuring a variety of technical and business related topics designed to help you grow your business, these friendly and informal meetings are held monthly.</p>
  <span class="btn">Find Now!</span>
</div>
<div class="city abs" role="img" aria-label="Photo of a city skyline beside a river at dusk"></div>
<div class="city-strip abs"></div>

<h2 class="section-h abs" style="top:3076px">Client Saying</h2>
<svg class="portrait-ring abs" width="248" height="248" viewBox="0 0 248 248"><path d="M124 10 A114 114 0 0 1 238 124" fill="none" stroke="#f37122" stroke-width="12"/><path d="M124 238 A114 114 0 0 1 10 124" fill="none" stroke="#2b2b2b" stroke-width="12"/></svg>
<div class="portrait abs" role="img" aria-label="Portrait of the quoted partner representative"></div>
<div class="quote-mark abs">&ldquo;</div>
<blockquote class="quote abs">Our partnership with Crestlane Tech Guild has helped Norvale better understand the needs of the SMB IT market and to showcase our solutions to technical experts in a meaningful and engaging way...
  <cite>Dale Corran &ndash; National Sales Manager<br>Norvale Systems Limited</cite>
</blockquote>
<div class="dots abs"><i class="on"></i><i></i><i></i><i></i></div>

<h2 class="news-h abs">In the News</h2>
<article class="news-card abs" style="left:176px">
  <div class="pic" role="img" aria-label="Abstract pale teal architectural curves" style="background:linear-gradient(135deg,#d5ecec,#8fc6c8)"></div>
  <div class="body"><div class="date">28 Mar 2017</div><h4>New Bronze Partner announcement &ndash; Multimedia Technology</h4></div>
</article>
<article class="news-card abs" style="left:472px">
  <div class="pic" role="img" aria-label="Photo of a man in a suit in an office" style="background:linear-gradient(160deg,#efefef,#8d8d8d)"></div>
  <div class="body"><div class="date">20 Mar 2017</div><h4>Welcome to our new CEO</h4></div>
</article>
<article class="news-card abs" style="left:764px">
  <div class="pic" role="img" aria-label="Photo of hands exchanging documents over a desk" style="background:linear-gradient(135deg,#f2e4cf,#b79a72)"></div>
  <div class="body"><div class="date">08 Mar 2017</div><h4>Sydney MSPs Connect Solutions and Available range</h4></div>
</article>

<footer class="footer abs">
  <div class="pitch abs"><strong>With combined revenue of over $150m,</strong><p>Crestlane Tech Guild is the peak body for IT business owners and professionals, servicing SMBs in Australia.</p></div>
  <span class="btn solid abs" style="left:764px">Become a Partner!</span>
  <span class="btn abs" style="left:930px">Join Now!</span>
  <div class="rule abs"></div>
  <div class="col abs" style="left:176px"><h5>Membership &amp; General enquiries</h5><div class="phone">Call. 1300 555 019</div><div>e. hello@crestlanetechguild.org</div><div>Contact Us</div></div>
  <div class="col abs" style="left:520px"><h5>Follow us</h5><div class="socials"><i></i><i></i><i></i><i></i><i></i></div></div>
  <div class="col abs" style="left:880px"><h5>&copy; 2020</h5><div>Crestlane Tech Guild Limited</div><div>All rights reserved.</div><div>Privacy Policy | Contact</div></div>
</footer>

</body>
</html>
```